Vintage Packaging Needed for Vintage Sports Equipment
We have 5 different boxes which require a similar packaging design. We have uploaded the design templates and logo.
Initially, please focus on the soccer ball first. Our products are vintage sports equipment that come with very nice wooden display mounts. The sport equipment can be played with or can be used as a display piece.
The logo color can be altered. We have not identified a brand color yet. We desire the branding and packaging to represent high quality vintage sport equipment. Many of the designs come from the early 1920s or earlier.
The products come in real leather or faux leather.
Example styles attached.
Target Market(s)
Youth, Adults, Business Offices - products used as desk pieces for show etc,
Requirements
Must have
- Must have company Logo.
- Must have placeholder for Bar Code
- Must have following text:
- Distributed By:
- Brackenfield Industries, LLC
- 5870 W Orchard Blvd
- #418
- Provo, UT 84019
- MADE IN INDIA WITH GLOBALLY SOURCED MATERIALS
- Brackenfield and True Heirloom are trademarks of Brackenfield Industries, LLC.
- © 2017, Brackenfield Industries, LLC. All rights reserved.
- Name of Sport Equipment in Package (Basketball, Soccer ball, etc)
- (warranty is preferably on the bottom of the packaging)
- Warranty
- BRACKENFIELD, warrants this product against defects in materials and workmanship under normal use for a period of ONE (1) YEAR from the date of retail purchase by the original end-user purchaser (“Warranty Period”). BRACKENFIELD MAKES NO OTHER WARRANTIES, EXPRESS OR IMPLIED, INCLUDING BU NOT LIMITED TO THE WARRANTIES OF MERCHANTABILITY OR FITNESS FOR A PARTICULAR PURPOSE. Original receipt required to validate warranty and all claims are subject to approval by BRACKENFIELD. BRACKENFIELD WILL NOT BE LIABLE FOR ANY SPECIAL, INCIDENTAL, OR CONSEQUENTIAL DAMAGES. BRACKENFIELD's liability with respect to a claim for any damages arising out of or connected with the sale, manufacture, use, inability to use, or performance of this product will be limited to replacement of the product only. Purchases should independently determine the suitability of each material for the specific purpose prior to use.
- We also need these in AI and PSD file formats.
Nice to have
- We'd like designers to take some liberty and add other elements as they see fit based on creativity or past experience in packaging.
- Website address of designer

```html
<!DOCTYPE html>
<html lang="en">
<head>
<meta charset="utf-8">
<title>Soccer Ball Box – Front Panel</title>
<link rel="stylesheet" href="https://fonts.googleapis.com/css2?family=Cinzel:wght@700;900&family=Lobster&display=swap">
<style>
  :root {
    --paper: #efe6d8;
    --kraft: #d6c3a4;
    --kraft-dark: #c9b491;
    --ink: #2b2022;
    --accent: #ee5236;
    --cream: #f6efe2;
  }
  html, body {
    margin: 0;
    padding: 0;
    width: 1200px;
    height: 1000px;
    overflow: hidden;
    background: var(--paper);
  }
  .canvas {
    position: relative;
    width: 1200px;
    height: 1000px;
  }
  .box-front {
    position: absolute;
    left: 290px;
    top: 180px;
    width: 620px;
    height: 640px;
    background: var(--kraft);
    overflow: hidden;
  }
  .dark-band {
    position: absolute;
    left: 0;
    top: 368px;
    width: 100%;
    height: 272px;
    background: var(--ink);
  }
  .frame-line {
    position: absolute;
    left: 26px;
    top: 18px;
    right: 30px;
    bottom: 24px;
    border: 4px solid var(--accent);
  }
  .product-script {
    position: absolute;
    left: 52px;
    top: 36px;
    margin: 0;
    font-family: "Lobster", cursive;
    font-weight: 400;
    font-size: 118px;
    line-height: 1;
    color: var(--accent);
    letter-spacing: -1px;
  }
  .product-word {
    position: absolute;
    left: 78px;
    top: 186px;
    margin: 0;
    font-family: "Cinzel", serif;
    font-weight: 900;
    font-size: 58px;
    line-height: 1;
    color: var(--accent);
    letter-spacing: 2px;
  }
  .ball-art {
    position: absolute;
    left: 420px;
    top: 128px;
    width: 190px;
    height: 210px;
  }
  .product-count {
    position: absolute;
    left: 66px;
    top: 400px;
    margin: 0;
    font-family: "Cinzel", serif;
    font-weight: 900;
    font-size: 44px;
    line-height: 1;
    color: var(--cream);
    letter-spacing: 3px;
  }
  .product-material {
    position: absolute;
    left: 68px;
    top: 462px;
    margin: 0;
    font-family: "Cinzel", serif;
    font-weight: 700;
    font-size: 22px;
    line-height: 1;
    color: var(--cream);
    letter-spacing: 2px;
  }
  .brand-tag {
    position: absolute;
    left: 230px;
    top: 528px;
    width: 128px;
    height: 112px;
    background: var(--accent);
    display: flex;
    align-items: center;
    justify-content: center;
  }
  .brand-name {
    font-family: "Cinzel", serif;
    font-weight: 700;
    font-size: 13px;
    color: var(--ink);
    letter-spacing: 0.5px;
    text-transform: uppercase;
    text-align: center;
    line-height: 1.2;
  }
</style>
</head>
<body>
  <div class="canvas">
    <section class="box-front">
      <div class="dark-band"></div>
      <div class="frame-line"></div>

      <h1 class="product-script">Soccer</h1>
      <h2 class="product-word">BALL</h2>

      <svg class="ball-art" viewBox="0 0 190 210" role="img" aria-label="Hand-drawn vintage leather soccer ball illustration">
        <ellipse cx="95" cy="105" rx="92" ry="102" fill="var(--kraft-dark)"/>
      </svg>

      <p class="product-count">ONE PIECE</p>
      <p class="product-material">GENUINE LEATHER</p>

      <div class="brand-tag">
        <span class="brand-name">True Heirloom</span>
      </div>
    </section>
  </div>
</body>
</html>
```